Letterhead & Business Card for our Professional Practice (Financial Services)

We are looking for someone to design a letterhead and business card for our business, which is a professional practice called Harbor Lumen Capital Limited. The website is at www.harborrlumencapital.example.co.uk.

The letterhead needs to have: (a) our logo (b) address (c) telephone number (d) email address and (e) our company number.

We would like the stationary to be consistent with the website.

I have attached the logo in EPS and PNG format.

Target Market(s)

Professional services, large commercial enterprises, financial services

Industry/Entity Type

Financial Service

Font styles to use
Serif

Colors
3176b5
f04a50

Requirements
Must have
• Be consistent with our website located at www.harborlumencapital.example.co.uk
• Be in the following formats:
• 1. Word template for the letterhead
• 2. PDF for the letterhead with setup and bleeds required at www.presskite.example.co.uk
• 3. PDF for the business card with setup and bleeds required at www.presskite.example.co.uk
Nice to have
• Something with a really interesting design that says "these guys are professional but dynamic and interesting"
Should not have
• Boring

```html
<!DOCTYPE html>
<html lang="en">
<head>
<meta charset="utf-8">
<title>Harbor Lumen Capital – Stationery</title>
<link href="https://fonts.googleapis.com/css2?family=Crimson+Text:wght@600&family=Open+Sans:wght@400;600;700&display=swap" rel="stylesheet">
<style>
:root{
  --navy:#0c3a6c;
  --red:#c1162b;
  --paper:#ffffff;
  --bg:#ebebeb;
  --ink:#3a3f47;
  --muted:#7c828b;
}
*{box-sizing:border-box;margin:0;padding:0}
html,body{width:1200px;height:874px;overflow:hidden;background:var(--bg)}
body{position:relative;font-family:"Open Sans",Arial,sans-serif;color:var(--ink)}
.sheet{position:absolute;background:var(--paper);box-shadow:0 2px 8px rgba(0,0,0,.12);overflow:hidden}
.brand{display:flex;align-items:center;gap:7px;font-family:"Crimson Text",Georgia,serif;font-weight:600;color:var(--navy);white-space:nowrap}
.brand-mark{background:var(--red);flex:none}
.brand.light{color:#fff}
.brand.light .brand-mark{background:#fff}

/* letterhead */
.letterhead{left:40px;top:40px;width:310px;height:438px}
.letterhead .brand{position:absolute;top:34px;left:0;right:0;justify-content:center;font-size:17px}
.letterhead .brand-mark{width:12px;height:12px}
.letter-body{position:absolute;top:110px;left:34px;right:34px;font-size:7.5px;line-height:1.6}
.letter-body p{margin-bottom:8px}
.signer{font-weight:700;margin-top:20px}
.lh-footer{position:absolute;left:0;right:0;bottom:0}
.lh-footer .rule{height:4px;background:var(--red)}
.lh-footer .band{background:var(--navy);color:#fff;font-size:6px;line-height:1;padding:7px 12px;display:flex;flex-direction:column;gap:6px}
.lh-footer .row{display:flex;justify-content:space-between;align-items:center}
.lh-footer .item{display:flex;align-items:center;gap:4px;white-space:nowrap}
.dot{width:5px;height:5px;background:var(--red);border-radius:50%;flex:none}

/* folder */
.folder{left:380px;top:40px;width:310px;height:438px}
.folder .brand{position:absolute;top:60px;left:0;right:0;justify-content:center;font-size:21px}
.folder .brand-mark{width:15px;height:15px}
.folder-panel{position:absolute;left:0;right:0;top:170px;height:200px;background:var(--navy)}
.folder-band{position:absolute;left:0;right:0;top:370px;bottom:0;background:var(--red);color:#fff;font-size:7.5px;display:flex;align-items:center;justify-content:center;letter-spacing:.3px}

/* envelopes */
.envelope-back{left:720px;top:40px;width:440px;height:220px}
.env-flap{position:absolute;left:0;right:0;top:0;height:92px;background:var(--navy);border-radius:0 0 28px 28px;display:flex;align-items:center;justify-content:center}
.env-flap .brand-mark{width:14px;height:14px;background:#fff}
.env-web{position:absolute;bottom:18px;left:0;right:0;text-align:center;font-size:7px;color:var(--muted)}
.envelope-front{left:720px;top:280px;width:440px;height:220px}
.envelope-front .brand{position:absolute;left:34px;top:100px;font-size:17px}
.envelope-front .brand-mark{width:12px;height:12px}
.env-address{position:absolute;left:53px;top:126px;font-size:7px;color:var(--muted);line-height:1.5}
.env-stripes{position:absolute;left:0;right:0;bottom:0}
.env-stripes .navy{height:12px;background:var(--navy)}
.env-stripes .red{height:6px;background:var(--red)}

/* business cards */
.card{width:250px;height:145px}
.card-front{left:380px;top:520px;background:var(--navy)}
.card-front .brand{position:absolute;top:48px;left:0;right:0;justify-content:center;font-size:17px}
.card-front .brand-mark{width:12px;height:12px}
.card-front .web{position:absolute;top:80px;left:0;right:0;text-align:center;color:#c9d4e3;font-size:6.5px}
.card-front .stripe{position:absolute;left:0;right:0;bottom:0;height:10px;background:var(--red)}
.card-back{left:650px;top:520px}
.card-back .brand{position:absolute;top:18px;right:18px;font-size:13px}
.card-back .brand-mark{width:9px;height:9px}
.person{position:absolute;left:18px;top:58px}
.person .name{font-size:9px;font-weight:700;color:var(--red);letter-spacing:.5px}
.person .role{font-size:6.5px;color:var(--muted)}
.card-back .band{position:absolute;left:0;right:0;bottom:0;height:44px;background:var(--navy);color:#fff;font-size:6px;padding:7px 18px;display:flex;justify-content:space-between;line-height:1.6;white-space:nowrap}
.card-back .rule{position:absolute;left:0;right:0;bottom:44px;height:4px;background:var(--red)}
.contact-line{display:flex;align-items:center;gap:4px}
.contact-line svg{width:7px;height:7px;flex:none}
.card-address{text-align:right}

/* notebook */
.notebook{left:40px;top:510px;width:310px;height:330px}
.notebook .brand{position:absolute;top:36px;left:0;right:0;justify-content:center;font-size:17px}
.notebook .brand-mark{width:12px;height:12px}
.nb-panel{position:absolute;left:0;right:0;top:120px;height:150px;background:var(--navy)}
.nb-band{position:absolute;left:0;right:0;top:270px;bottom:0;background:var(--red);color:#fff;font-size:6.5px;display:flex;align-items:center;justify-content:center}
.nb-spiral{position:absolute;left:6px;top:10px;bottom:10px;width:8px;background:repeating-linear-gradient(to bottom,#8a8f96 0 3px,transparent 3px 12px)}
</style>
</head>
<body>

<section class="sheet letterhead">
  <div class="brand"><span class="brand-mark"></span>Harbor Lumen Capital</div>
  <div class="letter-body">
    <p>Dear Sir,</p>
    <p>Thank you for your recent enquiry about our advisory services. We welcome the chance to review your current position and to outline a plan that suits your long term goals.</p>
    <p>Our team will contact you shortly to arrange a first meeting at a time that works for you.</p>
    <p>Yours sincerely,</p>
    <p class="signer">Clara Penwick</p>
  </div>
  <footer class="lh-footer">
    <div class="rule"></div>
    <div class="band">
      <div class="row">
        <span class="item"><span class="dot"></span>12 Quayside Row, Eastford, Kentshire, EF2 4QP</span>
        <span class="item"><span class="dot"></span>01632 960 418</span>
      </div>
      <div class="row">
        <span class="item"><span class="dot"></span>hello@harborlumencapital.example.co.uk</span>
        <span class="item"><span class="dot"></span>Company No. 08415263</span>
      </div>
      <div class="row">
        <span class="item"><span class="dot"></span>www.harborlumencapital.example.co.uk</span>
      </div>
    </div>
  </footer>
</section>

<section class="sheet folder">
  <div class="brand"><span class="brand-mark"></span>Harbor Lumen Capital</div>
  <div class="folder-panel"></div>
  <div class="folder-band">www.harborlumencapital.example.co.uk</div>
</section>

<section class="sheet envelope-back">
  <div class="env-flap"><span class="brand-mark"></span></div>
  <div class="env-web">www.harborlumencapital.example.co.uk</div>
</section>

<section class="sheet envelope-front">
  <div class="brand"><span class="brand-mark"></span>Harbor Lumen Capital</div>
  <div class="env-address">12 Quayside Row<br>Eastford, Kentshire, EF2 4QP</div>
  <div class="env-stripes"><div class="navy"></div><div class="red"></div></div>
</section>

<section class="sheet card card-front">
  <div class="brand light"><span class="brand-mark"></span>Harbor Lumen Capital</div>
  <div class="web">www.harborlumencapital.example.co.uk</div>
  <div class="stripe"></div>
</section>

<section class="sheet card card-back">
  <div class="brand"><span class="brand-mark"></span>Harbor Lumen Capital</div>
  <div class="person">
    <div class="name">OWEN MARLOWE</div>
    <div class="role">Account Executive</div>
  </div>
  <div class="rule"></div>
  <div class="band">
    <div>
      <div class="contact-line"><svg viewBox="0 0 10 10"><path d="M2 1h2l1 2-1.2 1a5 5 0 0 0 2.2 2.2L7 5l2 1v2a1 1 0 0 1-1 1A8 8 0 0 1 1 2a1 1 0 0 1 1-1z" fill="#fff"/></svg>01632 960 418</div>
      <div class="contact-line"><svg viewBox="0 0 10 10"><rect x="1" y="2" width="8" height="6" fill="none" stroke="#fff"/><path d="M1 2l4 3 4-3" fill="none" stroke="#fff"/></svg>hello@harborlumencapital.example.co.uk</div>
      <div class="contact-line"><svg viewBox="0 0 10 10"><circle cx="5" cy="5" r="4" fill="none" stroke="#fff"/></svg>www.harborlumencapital.example.co.uk</div>
    </div>
    <div class="card-address">12 Quayside Row<br>Eastford, Kentshire<br>EF2 4QP</div>
  </div>
</section>

<section class="sheet notebook">
  <div class="nb-spiral"></div>
  <div class="brand"><span class="brand-mark"></span>Harbor Lumen Capital</div>
  <div class="nb-panel"></div>
  <div class="nb-band">www.harborlumencapital.example.co.uk</div>
</section>

</body>
</html>
```